Trellivo business expansion job ad, join our team

Im needing a business expansion job Ad for trellivo. THis Ad will represent our car dealership hiring for multiple job positions which include. Automotive service positions, Sales consultants, collection agents, finance and underwriting and management. We are a Buy Here Pay Here dealership that is growing rapidly and moving into a new location, Business Expansion id a key term I would like to use. We are adding team members. We also need to be aware of Trellivos image sizing so it will appear well.

Target Market(s)

employment, job ad

Colors
0054AA
0677BA
7BADD7
CADEEF
E8F1F8

Requirements
Must have
• Business Expansion , Join our team
Nice to have
• our logo

```html
<!DOCTYPE html>
<html lang="en">
<head>
<meta charset="utf-8">
<title>Trellivo – Business Expansion, Join Our Team</title>
<link rel="stylesheet" href="https://fonts.googleapis.com/css2?family=Montserrat:wght@300;400;500;600;700;800;900&display=swap">
<style>
  :root{
    --blue-deep:#0054AA;
    --blue:#0677BA;
    --blue-soft:#7BADD7;
    --blue-pale:#CADEEF;
    --blue-mist:#E8F1F8;
    --ink:#1f2430;
    --ink-soft:#4a4f5a;
    --bg:#f3f4f6;
  }
  *{margin:0;padding:0;box-sizing:border-box}
  html,body{width:1200px;height:1200px;overflow:hidden}
  body{font-family:"Montserrat",sans-serif;background:var(--bg);color:var(--ink)}
  .ad{position:relative;width:1200px;height:1200px;overflow:hidden;
      background:linear-gradient(180deg,#fafbfc 0%,#eef0f3 55%,#e6e8eb 100%)}
  .ad__backdrop{position:absolute;inset:0;
      background:radial-gradient(ellipse at 25% 25%,rgba(200,205,210,.45),transparent 55%),
                 linear-gradient(180deg,transparent 55%,rgba(190,195,200,.35) 100%)}
  .ad__panel{position:absolute;left:451px;top:0;width:749px;height:700px;background:#fff;border-top-left-radius:140px}
  .ad__photo{position:absolute;left:451px;top:180px;width:749px;height:468px;
      background:linear-gradient(180deg,#c4ccd6 0%,#8a929c 40%,#3a3c41 70%,#141517 100%)}
  .brand{position:absolute;left:985px;top:76px;width:160px;text-align:center;
      font-weight:800;font-size:40px;color:var(--blue-deep);letter-spacing:-.5px}
  .kicker-rule{position:absolute;left:60px;top:225px;width:46px;height:1px;background:var(--ink-soft)}
  .kicker{position:absolute;left:60px;top:233px;font-size:15px;font-weight:400;color:var(--ink-soft);letter-spacing:.3px}
  .frame{position:absolute;left:0;top:0}
  .headline{position:absolute;left:96px;top:306px;line-height:1}
  .headline__lead{font-size:26px;font-weight:700;color:var(--ink);display:block}
  .headline__key{font-size:52px;font-weight:800;display:block;margin-top:2px;
      background:linear-gradient(180deg,var(--blue) 0%,var(--blue-deep) 100%);-webkit-background-clip:text;background-clip:text;-webkit-text-fill-color:transparent}
  .headline__sub{font-size:36px;font-weight:700;color:var(--ink);display:block;margin-top:-2px}
  .hiring-plate{position:absolute;left:451px;top:416px;width:170px;height:98px;background:#fff}
  .hiring{position:absolute;left:92px;top:398px;font-size:130px;font-weight:900;letter-spacing:-3px;line-height:1.05;
      background:linear-gradient(180deg,var(--blue) 0%,var(--blue-deep) 100%);-webkit-background-clip:text;background-clip:text;-webkit-text-fill-color:transparent}
  .tagline{position:absolute;left:97px;top:534px;font-size:32px;font-weight:400;color:var(--ink);letter-spacing:.5px}
  .tagline-rule{position:absolute;left:337px;top:554px;width:114px;height:2px;background:var(--ink)}
  .tagline-rule--light{left:451px;width:162px;background:#fff}
  .arrow{position:absolute;left:0;top:0}
  .roles{position:absolute;left:601px;top:726px;width:540px}
  .roles__intro{font-size:19px;font-weight:400;color:var(--ink-soft);line-height:30px}
  .role{position:absolute;display:flex;align-items:center}
  .role__tick{width:46px;height:46px;flex:none}
  .role__name{margin-left:16px;font-size:28px;font-weight:700;color:#1c2636;line-height:34px}
  .role__name span{background:linear-gradient(180deg,transparent 58%,var(--blue-pale) 58%)}
  .info{position:absolute;left:60px;display:flex;align-items:center}
  .info__icon{width:50px;height:50px;flex:none}
  .info__text{margin-left:23px}
  .info__label{font-size:20px;font-weight:400;color:var(--ink-soft);display:block}
  .info__value{font-size:23px;font-weight:600;color:var(--ink);display:block;margin-top:3px}
</style>
</head>
<body>
<main class="ad">
  <div class="ad__backdrop" role="img" aria-label="Faded view of the dealership parking lot"></div>
  <div class="ad__panel"></div>
  <div class="ad__photo" role="img" aria-label="Photo of the new dealership building and its parking lot"></div>

  <div class="brand">Trellivo</div>

  <div class="kicker-rule"></div>
  <p class="kicker">GOOD NEWS FOR YOU!</p>

  <svg class="frame" width="1200" height="1200" viewBox="0 0 1200 1200" aria-hidden="true">
    <path d="M333 292 V262 H63 V614 H333 V578" fill="none" stroke="var(--blue)" stroke-width="6"/>
  </svg>

  <h1 class="headline">
    <span class="headline__lead">WE ARE</span>
    <span class="headline__key">EXPANDING</span>
    <span class="headline__sub">OUR BUSINESS &amp;</span>
  </h1>
  <div class="hiring-plate"></div>
  <div class="hiring">HIRING.</div>

  <p class="tagline">Join our team</p>
  <div class="tagline-rule"></div>
  <div class="tagline-rule tagline-rule--light"></div>

  <svg class="arrow" width="1200" height="1200" viewBox="0 0 1200 1200" aria-hidden="true">
    <path d="M628 486 C680 520 712 560 722 608" fill="none" stroke="#fff" stroke-width="3" stroke-linecap="round"/>
    <path d="M690 600 L724 630 L748 596" fill="none" stroke="#fff" stroke-width="3" stroke-linecap="round" stroke-linejoin="round"/>
  </svg>

  <section class="roles">
    <p class="roles__intro">We are looking for professionals to fill the following vacate positions:</p>
  </section>

  <div class="role" style="left:604px;top:811px">
    <svg class="role__tick" viewBox="0 0 46 46"><circle cx="23" cy="23" r="23" fill="var(--blue-deep)"/><path d="M14 23 L20 29 L32 17" fill="none" stroke="#fff" stroke-width="3" stroke-linecap="round" stroke-linejoin="round"/></svg>
    <span class="role__name"><span>Automotive service positions</span></span>
  </div>
  <div class="role" style="left:604px;top:885px">
    <svg class="role__tick" viewBox="0 0 46 46"><circle cx="23" cy="23" r="23" fill="var(--blue-deep)"/><path d="M14 23 L20 29 L32 17" fill="none" stroke="#fff" stroke-width="3" stroke-linecap="round" stroke-linejoin="round"/></svg>
    <span class="role__name"><span>Sales consultants</span></span>
  </div>
  <div class="role" style="left:604px;top:960px">
    <svg class="role__tick" viewBox="0 0 46 46"><circle cx="23" cy="23" r="23" fill="var(--blue-deep)"/><path d="M14 23 L20 29 L32 17" fill="none" stroke="#fff" stroke-width="3" stroke-linecap="round" stroke-linejoin="round"/></svg>
    <span class="role__name"><span>Collection agents</span></span>
  </div>
  <div class="role" style="left:604px;top:1027px">
    <svg class="role__tick" viewBox="0 0 46 46"><circle cx="23" cy="23" r="23" fill="var(--blue-deep)"/><path d="M14 23 L20 29 L32 17" fill="none" stroke="#fff" stroke-width="3" stroke-linecap="round" stroke-linejoin="round"/></svg>
    <span class="role__name"><span>Finance and underwriting</span><br>and management</span>
  </div>

  <div class="info" style="top:856px">
    <svg class="info__icon" viewBox="0 0 50 50" fill="none" stroke="var(--ink)" stroke-width="2">
      <rect x="2" y="8" width="44" height="38" rx="3"/><line x1="2" y1="17" x2="46" y2="17"/>
      <line x1="12" y1="3" x2="12" y2="12"/><line x1="24" y1="3" x2="24" y2="12"/><line x1="36" y1="3" x2="36" y2="12"/>
      <rect x="8" y="22" width="5" height="4"/><rect x="17" y="22" width="5" height="4"/><rect x="26" y="22" width="5" height="4"/><rect x="35" y="22" width="5" height="4"/>
      <rect x="8" y="30" width="5" height="4"/><rect x="17" y="30" width="5" height="4"/><rect x="8" y="38" width="5" height="4"/>
      <circle cx="40" cy="40" r="8" fill="#fff"/><path d="M36 40 L39 43 L44 37"/>
    </svg>
    <div class="info__text"><span class="info__label">Hiring from</span><span class="info__value">1 Aug - 15 Aug 2021</span></div>
  </div>

  <div class="info" style="top:950px">
    <svg class="info__icon" viewBox="0 0 50 50" fill="none" stroke="var(--ink)" stroke-width="2">
      <circle cx="25" cy="25" r="23"/><ellipse cx="25" cy="25" rx="10" ry="23"/>
      <line x1="2" y1="25" x2="48" y2="25"/><path d="M6 13 H44 M6 37 H44"/><line x1="25" y1="2" x2="25" y2="48"/>
    </svg>
    <div class="info__text"><span class="info__label">For more information, visit</span><span class="info__value">www.trellivo.com</span></div>
  </div>

  <div class="info" style="top:1042px">
    <svg class="info__icon" viewBox="0 0 50 50" fill="none" stroke="var(--ink)" stroke-width="2">
      <rect x="2" y="2" width="46" height="46" rx="4"/>
    </svg>
    <div class="info__text"><span class="info__label">Checkout our Linkora page</span><span class="info__value">@trellivo</span></div>
  </div>
</main>
</body>
</html>
```